Modern HomePage Design for Church

We are looking for a modern homepage design using the sections we put together in the template. The colors we want are blue, black, grey, and white. We do not want use the colors in the logo. Please modify the logo color to match the website color scheme.

Target Market(s)

Church

Industry/Entity Type

Church

Number of Pages Required

1 page

Colors
0293ce
ffffff
474747
9d9d9d

```html
<!DOCTYPE html>
<html lang="en">
<head>
<meta charset="utf-8">
<title>Harvest Hill Church – Home</title>
<link rel="stylesheet" href="https://fonts.googleapis.com/css2?family=Poppins:wght@400;500;600;700&family=Playfair+Display:wght@700;900&family=Great+Vibes&family=Open+Sans:wght@400;600&display=swap">
<style>
:root{
  --blue:#0293ce;
  --blue-bright:#14a3e0;
  --white:#ffffff;
  --dark:#474747;
  --grey:#9d9d9d;
  --ink:#1c1c1c;
  --night:#232323;
  --text:#555555;
  --light:#f4f4f4;
}
*{box-sizing:border-box;margin:0;padding:0}
html,body{width:1200px;height:3319px;overflow:hidden}
body{position:relative;font-family:"Open Sans",Arial,sans-serif;color:var(--text);background:var(--white)}
.abs{position:absolute}
.btn{position:absolute;display:flex;align-items:center;justify-content:center;font:600 10px "Poppins",sans-serif;letter-spacing:.08em;text-transform:uppercase;color:var(--white);background:var(--blue)}
.btn.black{background:var(--ink)}
.photo{position:absolute}

/* nav */
.topnav{position:absolute;left:0;top:0;width:1200px;height:36px;background:rgba(28,28,28,.9);z-index:3}
.topnav ul{position:absolute;left:210px;top:0;display:flex;list-style:none;height:36px;align-items:center;gap:34px}
.topnav li{font:500 10px "Poppins",sans-serif;color:var(--white);letter-spacing:.05em}
.topnav li.active{color:var(--blue-bright)}
.topnav .btn{left:873px;top:5px;width:104px;height:26px}

/* hero */
.hero{position:absolute;left:0;top:0;width:1200px;height:474px;overflow:hidden}
.hero .photo{inset:0;background:radial-gradient(ellipse at 78% 45%,#e8c7a8 0%,#b98a62 22%,#6e5a2c 48%,#3c4a22 72%,#1e2a14 100%)}
.hero-badges{position:absolute;top:56px;left:760px;display:flex;gap:8px}
.hero-badges span{background:var(--blue);color:var(--white);font:500 8px "Poppins",sans-serif;padding:5px 8px}
.brand{position:absolute;left:254px;top:100px;display:flex;align-items:center;gap:10px;font:600 28px "Poppins",sans-serif;color:var(--white);letter-spacing:.04em}
.brand i{display:block;width:14px;height:14px;background:var(--blue)}
.hero-script{position:absolute;left:0;width:800px;text-align:center;top:160px;font:32px "Great Vibes",cursive;color:var(--white)}
.hero-title{position:absolute;left:0;width:800px;text-align:center;top:200px;font:900 52px "Playfair Display",serif;color:var(--white);letter-spacing:.02em}
.hero-sub{position:absolute;left:0;width:800px;text-align:center;top:262px;font:700 25px "Poppins",sans-serif;color:var(--white);letter-spacing:.03em}
.hero-time{position:absolute;left:0;width:800px;text-align:center;top:302px;font:500 16px "Poppins",sans-serif;color:var(--white);letter-spacing:.05em}
.hero .btn{left:346px;top:347px;width:126px;height:33px}

/* welcome */
.welcome{position:absolute;left:0;top:474px;width:1200px;height:378px;background:var(--white)}
.welcome h1{position:absolute;left:62px;top:40px;font:600 30px "Poppins",sans-serif;color:var(--blue)}
.welcome .lead{position:absolute;left:62px;top:84px;font:600 11px "Poppins",sans-serif;color:var(--ink)}
.welcome hr{position:absolute;left:62px;top:116px;width:680px;border:0;border-top:2px solid #bdbdbd}
.welcome p{position:absolute;left:62px;width:680px;font-size:11px;line-height:1.6}
.welcome .sign{position:absolute;left:62px;top:280px;font:34px "Great Vibes",cursive;color:var(--ink)}
.welcome .photo{left:850px;top:8px;width:240px;height:346px;background:linear-gradient(180deg,#f2f2f2,#c8c8c8 30%,#3b3b3b 60%,#2a2a2a)}

/* meeting */
.meeting{position:absolute;left:0;top:852px;width:1200px;height:188px;background:var(--dark);color:var(--white)}
.meeting h2{position:absolute;left:200px;width:440px;text-align:center;top:44px;font:600 21px "Poppins",sans-serif;letter-spacing:.03em}
.meeting .date{position:absolute;left:200px;width:440px;text-align:center;top:74px;font-size:11px;color:#cfcfcf}
.meeting .desc{position:absolute;left:200px;width:440px;text-align:center;top:110px;font-size:11px;line-height:1.5;color:#e0e0e0}
.counter{position:absolute;top:38px;width:56px;text-align:center}
.counter small{display:block;font:500 8px "Poppins",sans-serif;color:var(--grey);letter-spacing:.1em}
.counter b{display:block;font:600 27px "Poppins",sans-serif;margin-top:2px}
.meeting .btn{left:773px;top:113px;width:106px;height:30px}

/* beliefs */
.beliefs{position:absolute;left:0;top:1040px;width:1200px;height:437px;overflow:hidden}
.beliefs .photo{inset:0;background:linear-gradient(100deg,#f5f1ee 0%,#e6dcd6 30%,#efe6e2 55%,#f3ecea 80%,#f6d9d6 100%)}
.belief{position:absolute;top:60px;width:300px;text-align:center;color:var(--ink)}
.belief svg{display:block;margin:0 auto 30px;width:64px;height:64px}
.belief h3{font:600 17px "Poppins",sans-serif;letter-spacing:.04em;margin-bottom:12px}
.belief p{font-size:10.5px;line-height:1.65;color:#333;height:70px}
.belief .btn{position:relative;margin:18px auto 0;width:106px;height:30px}

/* ministries */
.ministries{position:absolute;left:0;top:1477px;width:1200px;height:328px;background:var(--white)}
.ministries .photo{position:absolute}
.tag{position:absolute;background:var(--blue);color:var(--white);font:500 9px "Poppins",sans-serif;padding:5px 9px}
.involve{position:absolute;left:815px;top:0;width:385px;height:328px;background:var(--night);text-align:center}
.involve h3{margin-top:105px;font:500 21px "Poppins",sans-serif;color:var(--white)}
.involve p{width:250px;margin:16px auto 0;font-size:11px;line-height:1.75;color:#6d6d6d}
.involve .btn{left:152px;top:232px;width:106px;height:30px}

/* blog */
.blog{position:absolute;left:0;top:1805px;width:1200px;height:310px;background:var(--white)}
.blog-card{position:absolute;left:170px;top:38px;width:346px;height:250px}
.blog-card .head{height:62px;background:var(--ink);color:var(--white);font:600 28px "Poppins",sans-serif;display:flex;align-items:center;justify-content:center;letter-spacing:.05em}
.blog-card .body{height:188px;background:var(--blue);color:var(--white);text-align:center;padding-top:28px}
.blog-card h3{font:500 21px "Poppins",sans-serif}
.blog-card p{width:270px;margin:12px auto 0;font-size:11px;line-height:1.7}
.blog h2{position:absolute;left:536px;top:62px;font:600 30px "Poppins",sans-serif;color:var(--blue);letter-spacing:.02em}
.blog hr{position:absolute;left:536px;top:104px;width:490px;border:0;border-top:2px solid var(--blue)}
.blog p.txt{position:absolute;left:536px;width:490px;font-size:10.5px;line-height:1.6}
.blog .btn{left:536px;top:230px;width:106px;height:30px}

/* pastor */
.pastor{position:absolute;left:0;top:2115px;width:1200px;height:380px;overflow:hidden;color:var(--white)}
.pastor .photo.bg{inset:0;background:radial-gradient(ellipse at 40% 60%,#6b5648 0%,#3e332c 45%,#1d1a18 100%)}
.label{position:absolute;font:600 13px "Poppins",sans-serif;letter-spacing:.04em}
.label-rule{position:absolute;border-top:1px solid rgba(255,255,255,.5)}
.pastor .portrait{left:162px;top:98px;width:186px;height:232px;border:4px solid var(--white);background:linear-gradient(160deg,#bfc6cc,#7a8790 55%,#4f5b63)}
.pastor blockquote{position:absolute;left:376px;top:100px;width:310px;font:500 27px "Poppins",sans-serif;line-height:1.25}
.pastor p{position:absolute;left:376px;top:190px;width:320px;font-size:10.5px;line-height:1.6;color:#e6e6e6}
.pastor .by{position:absolute;left:376px;top:297px;font:600 11px "Poppins",sans-serif}
.podcast{position:absolute;left:748px;width:270px}
.podcast .play{position:absolute;left:0;top:0;width:26px;height:26px;border:1px solid rgba(255,255,255,.7);display:flex;align-items:center;justify-content:center}
.podcast h4{position:absolute;left:40px;top:6px;font:600 12px "Poppins",sans-serif;white-space:nowrap}
.podcast span{position:absolute;left:0;top:36px;font-size:10px;color:#ddd}
.podcast span b{color:var(--blue-bright);font-weight:400}

/* events */
.events{position:absolute;left:0;top:2495px;width:1200px;height:487px;background:var(--white)}
.event{position:absolute;width:470px;height:180px}
.event .photo{left:0;top:0;width:220px;height:150px;background:linear-gradient(90deg,#5a3b22,#a66a3c 40%,#3b3430 70%,#a33a30)}
.event .datebar{position:absolute;left:0;top:140px;width:220px;height:38px;background:var(--ink);color:var(--white);display:flex;align-items:center}
.event .datebar b{font:600 19px "Poppins",sans-serif;padding:0 10px}
.event .datebar span{border-left:1px solid #777;padding-left:10px;font-size:9px}
.event h4{position:absolute;left:236px;top:8px;width:210px;font:600 14px "Poppins",sans-serif;color:var(--ink);line-height:1.3}
.event ul{position:absolute;left:236px;top:56px;list-style:none;font-size:10px;line-height:1.5;color:#444}
.event li{display:flex;gap:7px;margin-bottom:6px}
.event li svg{flex:none;margin-top:3px}
.event .btn{left:236px;top:146px;width:106px;height:28px}

/* footer */
.footer{position:absolute;left:0;top:2982px;width:1200px;height:317px;background:var(--night);color:var(--white)}
.footer .col-title{position:absolute;top:42px;font:600 10px "Poppins",sans-serif;letter-spacing:.04em}
.sermon{position:absolute;width:240px;height:60px}
.sermon .thumb{position:absolute;left:0;top:0;width:46px;height:42px;background:linear-gradient(135deg,#6f7d88,#3c464e)}
.sermon h5{position:absolute;left:62px;top:0;font:500 9px "Poppins",sans-serif;color:var(--blue-bright);white-space:nowrap}
.sermon p{position:absolute;left:62px;top:16px;width:170px;font-size:9px;line-height:1.5;color:#8a8a8a}
.tags{position:absolute;left:487px;top:80px;width:210px;display:flex;flex-wrap:wrap;gap:6px}
.tags span{background:var(--blue);font-size:9px;padding:3px 8px}
.feed{position:absolute;left:487px;top:180px;width:222px;height:96px;background:linear-gradient(180deg,#4a4d55,#2d2f35);display:flex;align-items:center;justify-content:center;font:500 13px "Poppins",sans-serif}
.copyright{position:absolute;left:0;top:3299px;width:1200px;height:20px;background:#111;color:#aaa;font-size:9px;display:flex;align-items:center;justify-content:center}
</style>
</head>
<body>

<nav class="topnav">
  <ul>
    <li class="active">HOME</li><li>TEAM</li><li>FEATURES</li><li>EVENTS</li><li>SERMONS</li><li>CONTACTS</li><li>BLOG</li>
  </ul>
  <span class="btn">Donate Online</span>
</nav>

<header class="hero">
  <div class="photo" role="img" aria-label="Woman praying with folded hands in soft sunlit garden"></div>
  <div class="hero-badges"><span>SUNDAY WORSHIP 10:15</span><span>SUNDAY SCHOOL 9AM</span></div>
  <div class="brand"><i></i>WELLSPRING GRACE</div>
  <div class="hero-script">A Very Special Celebration Is Near</div>
  <div class="hero-title">EASTER WEEK</div>
  <div class="hero-sub">JOIN THE REMEMBERANCE</div>
  <div class="hero-time">SERVICES STARTING AT 19.00 DAILY</div>
  <span class="btn">Know More</span>
</header>

<section class="welcome">
  <h1>Welcome to Harvest Hill Church</h1>
  <div class="lead">We are a Community who firmly believes in Gods word. Come journey with us.</div>
  <hr>
  <p style="top:138px">Lorem ipsum dolor sit amet, consectetur adipiscing elit. Mauris lacinia vestibulum tellus, ut porttitor magna egestas vel. Donec vel justo mollis, adipiscing nibh quis, consectetur tellus. Aliquam et sagittis enim. Aliquam ac bibendum magna, quis luctus diam. Nulla facilisi.</p>
  <p style="top:222px">In id mi eu mi gravida placerat ac vitae quam. Class aptent taciti sociosqu ad litora torquent per conubia nostra, per inceptos himenaeos. Curabitur pharetra risus in elit luctus, sit amet volutpat diam mollis.</p>
  <div class="sign">Pastor Reed</div>
  <div class="photo" role="img" aria-label="Pastor couple standing together, smiling"></div>
</section>

<section class="meeting">
  <h2>CHURCH LEADERS MEETING</h2>
  <div class="date">March 27, 2019 7:00 pm</div>
  <div class="desc">Meeting for the church leader, this is where we plan the strategy for the church and give feedback on projects.</div>
  <div class="counter" style="left:686px"><small>DAYS</small><b>06</b></div>
  <div class="counter" style="left:763px"><small>HOURS</small><b>06</b></div>
  <div class="counter" style="left:841px"><small>MINS</small><b>06</b></div>
  <div class="counter" style="left:918px"><small>SECS</small><b>06</b></div>
  <span class="btn">Read More</span>
</section>

<section class="beliefs">
  <div class="photo" role="img" aria-label="Faded close-up of a weathered wooden cross"></div>
  <div class="belief" style="left:145px">
    <svg viewBox="0 0 64 64" fill="none" stroke="#1c1c1c" stroke-width="2.2"><path d="M32 54 10 32a12 12 0 0 1 22-15 12 12 0 0 1 22 15Z"/><path d="M8 32h14l4-8 6 16 5-12 3 4h16"/></svg>
    <h3>WHAT WE BELIEVE?</h3>
    <p>We believe the existence of god and His Holy Word to be the foundation of our faith, it shall not be moved nor be compromised.</p>
    <span class="btn black">Read More</span>
  </div>
  <div class="belief" style="left:448px">
    <svg viewBox="0 0 64 64" fill="none" stroke="#1c1c1c" stroke-width="2.2"><circle cx="32" cy="32" r="26"/><path d="M32 16v16l10 8"/></svg>
    <h3>SERVICES &amp; LOCATION</h3>
    <p>Riverton RV 10452<br><b>Sunday Morning  8:15–12:00 AM</b><br><b>Sunday Afternoon 4:00–6:00 AM</b><br><b>Wednesday 6:30–9:00 PM</b></p>
    <span class="btn black">Browse More</span>
  </div>
  <div class="belief" style="left:758px">
    <svg viewBox="0 0 64 64" fill="#1c1c1c"><path d="M32 30 22 20a6 6 0 0 1 10-7 6 6 0 0 1 10 7Z"/><path d="M6 40h10l10 4h12a3 3 0 0 1 0 6H28v2h12l14-8a3 3 0 0 1 4 4L42 58H20L6 52Z"/></svg>
    <h3>WATCH LIVE</h3>
    <p>By God's grace, we are glad to deliver an online live streaming services just for you. Join us by watching live every sunday and wednes day.</p>
    <span class="btn black">Watch Live</span>
  </div>
</section>

<section class="ministries">
  <div class="photo" style="left:0;top:0;width:492px;height:161px;background:linear-gradient(90deg,#c9a98a,#e2c7ad 40%,#8a7b6d)" role="img" aria-label="Young boy smiling outdoors"></div>
  <span class="tag" style="left:198px;top:124px">Teens Ministry</span>
  <div class="photo" style="left:496px;top:0;width:158px;height:161px;background:linear-gradient(160deg,#b36a3e,#6b3e2a)" role="img" aria-label="Girl in headscarf smiling"></div>
  <span class="tag" style="left:528px;top:106px">Teens Ministry</span>
  <div class="photo" style="left:656px;top:0;width:157px;height:161px;background:linear-gradient(160deg,#8a3a34,#3b2c2e)" role="img" aria-label="Group of teenagers together"></div>
  <span class="tag" style="left:688px;top:106px">Teens Ministry</span>
  <div class="photo" style="left:0;top:164px;width:168px;height:164px;background:linear-gradient(160deg,#c9922e,#5e3b1c)" role="img" aria-label="Senior couple walking in autumn park"></div>
  <span class="tag" style="left:38px;top:273px">Senior Ministry</span>
  <div class="photo" style="left:172px;top:164px;width:160px;height:164px;background:linear-gradient(160deg,#7a2e28,#2e1c1c)" role="img" aria-label="Person reading a bible"></div>
  <span class="tag" style="left:204px;top:273px">Teens Ministry</span>
  <div class="photo" style="left:336px;top:164px;width:156px;height:164px;background:linear-gradient(160deg,#8b3229,#2a1a1a)" role="img" aria-label="Open bible on a table"></div>
  <span class="tag" style="left:368px;top:273px">Bible Ministry</span>
  <div class="photo" style="left:496px;top:164px;width:317px;height:164px;background:linear-gradient(90deg,#4f5a38,#b58f72 55%,#7a6a45)" role="img" aria-label="Woman praying outdoors"></div>
  <span class="tag" style="left:602px;top:273px">Prayer Ministry</span>
  <div class="involve">
    <h3>Get Involved</h3>
    <p>The success iof our church depend on participation from people like you. Get involved in our Ministries – it will change your life.</p>
    <span class="btn">Read More</span>
  </div>
</section>

<section class="blog">
  <div class="blog-card">
    <div class="head">BLOG</div>
    <div class="body">
      <h3>Get Involved</h3>
      <p>The success iof our church depend on participation from people like you. Get involved in our Ministries – it will change your life.</p>
    </div>
  </div>
  <h2>PRAY WITHOURT CEASING</h2>
  <hr>
  <p class="txt" style="top:120px">Phasellus tempus risus vitae massa pellentesque aliquam eu nec est. Pellentesque habitant morbi tristique senectus et netus et malesuada fames ac turpis egestas. Sed non turpis imperdiet, ultricies eros id, ultrices ante. Duis maximus rutrum mauris, ac fermentum eros auctor quis.</p>
  <p class="txt" style="top:174px">Aliquam in quam consectetur diam gravida pretium. Suspendisse tellus nibh, luctus eu arcu at, tempor tincidunt nulla. Donec porta ex fermentum malesuada ultricies. Mauris sodales sagittis fringilla. Vivamus eget orci nisl. Curabitur non ante sagittis, accumsan nunc et, viverra felis.</p>
  <span class="btn black">Read More</span>
</section>

<section class="pastor">
  <div class="photo bg" role="img" aria-label="Dark close-up of an old wooden cross"></div>
  <div class="label" style="left:162px;top:30px">PASTOR</div>
  <div class="label-rule" style="left:162px;top:60px;width:520px"></div>
  <div class="photo portrait" role="img" aria-label="Portrait of senior pastor"></div>
  <blockquote>“One thing I ask of the Lord”</blockquote>
  <p>This is what I seek, that I may dwell in the house of the Lord all the days of my life, to gaze upon the beauty of the lord and to seek him in his temple. Taste and see that the lord is good; blessed is the man who takes refuge in him. The Lord is everlasting god, the creator of all the ends of the earth.</p>
  <div class="by">Samuel Whitford</div>
  <div class="label" style="left:748px;top:30px">PODCASTS</div>
  <div class="label-rule" style="left:748px;top:60px;width:272px"></div>
  <div class="podcast" style="top:100px"><div class="play"><svg width="8" height="10" viewBox="0 0 8 10"><path d="M0 0l8 5-8 5z" fill="#fff"/></svg></div><h4>HOLY SPIRIT: STRATEGIC THINKING</h4><span>by <b>Nora Ellis</b></span></div>
  <div class="label-rule" style="left:748px;top:158px;width:272px"></div>
  <div class="podcast" style="top:176px"><div class="play"><svg width="8" height="10" viewBox="0 0 8 10"><path d="M0 0l8 5-8 5z" fill="#fff"/></svg></div><h4>HOLY SPIRIT: STRATEGIC THINKING</h4><span>by <b>Nora Ellis</b></span></div>
  <div class="label-rule" style="left:748px;top:234px;width:272px"></div>
  <div class="podcast" style="top:254px"><div class="play"><svg width="8" height="10" viewBox="0 0 8 10"><path d="M0 0l8 5-8 5z" fill="#fff"/></svg></div><h4>HOLY SPIRIT: STRATEGIC THINKING</h4><span>by <b>Nora Ellis</b></span></div>
  <div class="label-rule" style="left:748px;top:312px;width:272px"></div>
</section>

<section class="events">
  <article class="event" style="left:162px;top:40px">
    <div class="photo" role="img" aria-label="Weathered wooden cross against red background"></div>
    <div class="datebar"><b>22ND</b><span>APR 2019</span></div>
    <h4>SHARING OUR FAITH &amp; LOVE TO CHILDREN</h4>
    <ul>
      <li><svg width="9" height="9" viewBox="0 0 10 10"><circle cx="5" cy="5" r="4" fill="none" stroke="#444"/><path d="M5 2.5V5h2" stroke="#444" fill="none"/></svg>Thursday, 0800 AM – 0900 AM</li>
      <li><svg width="9" height="9" viewBox="0 0 10 10"><path d="M1 9V4l4-3 4 3v5z" fill="#444"/></svg>St. Mercy Chapel</li>
      <li><svg width="9" height="11" viewBox="0 0 10 12"><path d="M5 12S1 7 1 4.5a4 4 0 0 1 8 0C9 7 5 12 5 12z" fill="#444"/></svg>Linden Row, Riverton,<br>United States, 10452</li>
    </ul>
    <span class="btn">Read More</span>
  </article>
  <article class="event" style="left:624px;top:40px">
    <div class="photo" role="img" aria-label="Weathered wooden cross against red background"></div>
    <div class="datebar"><b>22ND</b><span>APR 2019</span></div>
    <h4>SHARING OUR FAITH &amp; LOVE TO CHILDREN</h4>
    <ul>
      <li><svg width="9" height="9" viewBox="0 0 10 10"><circle cx="5" cy="5" r="4" fill="none" stroke="#444"/><path d="M5 2.5V5h2" stroke="#444" fill="none"/></svg>Thursday, 0800 AM – 0900 AM</li>
      <li><svg width="9" height="9" viewBox="0 0 10 10"><path d="M1 9V4l4-3 4 3v5z" fill="#444"/></svg>St. Mercy Chapel</li>
      <li><svg width="9" height="11" viewBox="0 0 10 12"><path d="M5 12S1 7 1 4.5a4 4 0 0 1 8 0C9 7 5 12 5 12z" fill="#444"/></svg>Linden Row, Riverton,<br>United States, 10452</li>
    </ul>
    <span class="btn">Read More</span>
  </article>
  <article class="event" style="left:162px;top:261px">
    <div class="photo" role="img" aria-label="Weathered wooden cross against red background"></div>
    <div class="datebar"><b>22ND</b><span>APR 2019</span></div>
    <h4>SHARING OUR FAITH &amp; LOVE TO CHILDREN</h4>
    <ul>
      <li><svg width="9" height="9" viewBox="0 0 10 10"><circle cx="5" cy="5" r="4" fill="none" stroke="#444"/><path d="M5 2.5V5h2" stroke="#444" fill="none"/></svg>Thursday, 0800 AM – 0900 AM</li>
      <li><svg width="9" height="9" viewBox="0 0 10 10"><path d="M1 9V4l4-3 4 3v5z" fill="#444"/></svg>St. Mercy Chapel</li>
      <li><svg width="9" height="11" viewBox="0 0 10 12"><path d="M5 12S1 7 1 4.5a4 4 0 0 1 8 0C9 7 5 12 5 12z" fill="#444"/></svg>Linden Row, Riverton,<br>United States, 10452</li>
    </ul>
    <span class="btn">Read More</span>
  </article>
  <article class="event" style="left:624px;top:261px">
    <div class="photo" role="img" aria-label="Weathered wooden cross against red background"></div>
    <div class="datebar"><b>22ND</b><span>APR 2019</span></div>
    <h4>SHARING OUR FAITH &amp; LOVE TO CHILDREN</h4>
    <ul>
      <li><svg width="9" height="9" viewBox="0 0 10 10"><circle cx="5" cy="5" r="4" fill="none" stroke="#444"/><path d="M5 2.5V5h2" stroke="#444" fill="none"/></svg>Thursday, 0800 AM – 0900 AM</li>
      <li><svg width="9" height="9" viewBox="0 0 10 10"><path d="M1 9V4l4-3 4 3v5z" fill="#444"/></svg>St. Mercy Chapel</li>
      <li><svg width="9" height="11" viewBox="0 0 10 12"><path d="M5 12S1 7 1 4.5a4 4 0 0 1 8 0C9 7 5 12 5 12z" fill="#444"/></svg>Linden Row, Riverton,<br>United States, 10452</li>
    </ul>
    <span class="btn">Read More</span>
  </article>
</section>

<footer class="footer">
  <div class="col-title" style="left:162px">LATEST SERMONS</div>
  <div class="sermon" style="left:162px;top:80px"><div class="thumb" role="img" aria-label="Sermon speaker thumbnail"></div><h5>ALL THINGS ARE POSSIBLE</h5><p>Lorem ipsum dolor sit amet, consectetur adipiscing elit.</p></div>
  <div class="sermon" style="left:162px;top:160px"><div class="thumb" role="img" aria-label="Sermon speaker thumbnail"></div><h5>ABOUNDING IN THE WORK OF THE LORD</h5><p>Lorem ipsum dolor sit amet, consectetur adipiscing elit.</p></div>
  <div class="col-title" style="left:487px">SERMON TAGS</div>
  <div class="tags"><span>faith</span><span>forgiveness</span><span>goodheartedness</span><span>kindness</span><span>love</span><span>peace</span><span>trust</span><span>understanding</span><span>responsibility</span></div>
  <div class="feed" role="img" aria-label="Mountain landscape at dusk">Podcast Feed</div>
  <div class="col-title" style="left:780px">LATEST SERMONS</div>
  <div class="sermon" style="left:780px;top:80px"><div class="thumb" role="img" aria-label="Sermon speaker thumbnail"></div><h5>ALL THINGS ARE POSSIBLE</h5><p>Lorem ipsum dolor sit amet, consectetur adipiscing elit.</p></div>
  <div class="sermon" style="left:780px;top:160px"><div class="thumb" role="img" aria-label="Sermon speaker thumbnail"></div><h5>ABOUNDING IN THE WORK OF THE LORD</h5><p>Lorem ipsum dolor sit amet, consectetur adipiscing elit.</p></div>
</footer>
<div class="copyright">© 2019. All Rights Reserved. Wellspring Grace Church</div>

</body>
</html>
```